Need a website to promote and sell my book

Using images from the book, I need a website designed that helps promote the book and eventually sell it.
*Need a landing page
*About the author page
*Storefront page to purchase
*Coming soon page
*"Featured in" page that can link to news articles etc.
The images posted here are examples, the winner of the contest will get the images from the finished book. I will provide the exact text to the winner of the contest.

I can also provide images of kids reading the book. For now, I'll just use one, the winner can have them all to choose from.
Updates

Extending deadline to allow for a few more designers to submit and to allow time for me to review and hold a poll

Target Market(s)

Parents, aunts, uncles, grandparents, friends who have kids; teachers, daycare teachers, babysitters etc.

Industry/Entity Type

Custom Publishing

Coding

Coded - Design and coding required

Number of Pages Required

5+ page

Font styles to use
Sans Serif

Colors

Designer to choose colors to be used in the design.

Requirements
Must have
• It must have a fun feel like the book.
Nice to have
• Would be great to have a section that automatically pulls tweets about the book into it.

```html
<!DOCTYPE html>
<html lang="en">
<head>
<meta charset="utf-8">
<title>Melanie Trent, PhD — Children's Chemistry Book</title>
<link rel="stylesheet" href="https://fonts.googleapis.com/css2?family=Nunito:wght@400;600;700;800;900&display=swap">
<style>
:root{
  --orange:#fd9a3d;
  --blue:#2f7ae5;
  --white:#ffffff;
  --ink:#1f2530;
  --text:#5b5b5b;
  --cream:#f8efe4;
  --tan:#e6b577;
  --sky:#86d0f0;
  --sky-deep:#35a9e6;
  --pink:#ec2f86;
  --coral:#ea5f48;
}
*{box-sizing:border-box;margin:0;padding:0}
html,body{width:1200px;height:2211px;overflow:hidden}
body{position:relative;background:var(--white);font-family:"Nunito",sans-serif;color:var(--text)}
.abs{position:absolute}
.band{position:absolute;left:0;width:1200px;display:block}

/* header */
.site-name{left:250px;top:14px;color:var(--white);font-weight:800;font-size:17px}
.nav{left:640px;top:18px;display:flex;gap:22px;list-style:none}
.nav a{color:var(--white);font-weight:800;font-size:12px;text-decoration:none;display:block;padding-bottom:16px}
.nav a.active{color:var(--blue);border-bottom:2px solid var(--blue)}
.header-line{left:0;top:53px;width:1200px;height:1px;background:rgba(255,255,255,.25)}

/* hero */
.hero-photo{left:250px;top:96px;width:380px;height:278px;border-radius:16px;background:linear-gradient(135deg,#6f6a66 0%,#a7a09b 55%,#d7c7b0 100%)}
.hero-cover{left:480px;top:152px;width:154px;height:234px;border-radius:6px;background:linear-gradient(160deg,#5cc3ee 0%,#7fd2f1 60%,#f1c27a 100%);box-shadow:0 6px 14px rgba(0,0,0,.25)}
.hero-title{left:663px;top:90px;font-weight:900;font-size:36px;line-height:44px;color:var(--white)}
.hero-title .hl{color:var(--blue)}
.hero-text{left:663px;top:236px;width:290px;font-size:13px;line-height:20px;color:var(--white)}
.btn{position:absolute;display:flex;align-items:center;justify-content:center;border-radius:22px;font-weight:800;font-size:16px;text-decoration:none}
.btn-hero{left:663px;top:312px;width:170px;height:42px;background:var(--white);color:var(--orange)}

/* about */
.section-title{font-weight:900;font-size:35px;line-height:44px}
.about-title{left:250px;top:542px;color:var(--orange)}
.body-copy{font-size:13.5px;line-height:20.5px;color:var(--text)}
.about-copy{left:250px;top:597px;width:340px}
.btn-about{left:250px;top:762px;width:168px;height:43px;background:var(--orange);color:var(--white)}
.about-frame{left:606px;top:513px;width:334px;height:347px;border:2px dashed var(--pink);border-radius:14px}
.about-photo{left:618px;top:523px;width:309px;height:328px;border-radius:14px;background:linear-gradient(150deg,#3a4150 0%,#8a8d96 60%,#d2d3d7 100%)}
.about-badge{left:782px;top:492px;width:168px;height:158px;border-radius:10px;background:var(--pink);box-shadow:0 0 0 3px #f56fae inset}

/* book */
.book-cover{left:320px;top:955px;width:238px;height:345px;border-radius:4px;background:linear-gradient(170deg,#5ec7f0 0%,#7fd2f1 60%,#efc57f 100%);box-shadow:-30px 40px 40px rgba(0,0,0,.12)}
.book-title{left:593px;top:1002px;color:var(--tan)}
.book-copy{left:593px;top:1057px;width:340px}
.btn-book{left:593px;top:1220px;width:170px;height:43px;background:var(--tan);color:var(--white)}

/* stats */
.stats{left:0;top:1410px;width:1200px;display:flex;justify-content:center}
.stat{width:178px;text-align:center;color:var(--white)}
.stat-num{font-weight:900;font-size:34px;line-height:38px}
.stat-label{font-weight:800;font-size:12px}

/* articles */
.articles-title{left:0;top:1562px;width:1200px;text-align:center;color:var(--ink)}
.articles-intro{left:370px;top:1618px;width:460px;text-align:center;font-size:13.5px;line-height:19px;color:var(--ink)}
.card{position:absolute;top:1677px;width:221px;text-align:center}
.card-img{height:148px;border-radius:14px}
.card h3{margin-top:12px;font-weight:800;font-size:13.5px;line-height:17px;color:var(--ink)}
.card p{margin-top:9px;font-size:12px;line-height:16px;color:var(--ink)}
.card svg{margin-top:10px}

/* footer */
.footer-name{left:0;top:2044px;width:1200px;text-align:center;color:var(--white);font-weight:800;font-size:17px}
.social{left:0;top:2083px;width:1200px;display:flex;justify-content:center;gap:10px;list-style:none}
.social li{width:42px;height:42px;border-radius:50%;border:3px solid var(--white)}
.copyright{left:0;top:2183px;width:1200px;text-align:center;font-size:10px;color:var(--ink)}
</style>
</head>
<body>

<!-- Header + hero band -->
<svg class="band" style="top:0" width="1200" height="460" viewBox="0 0 1200 460" aria-hidden="true">
  <path d="M0 0H1200V440C1080 455 980 420 860 418C720 416 650 452 480 446C330 440 220 410 120 414C70 416 30 425 0 430Z" fill="var(--orange)"/>
</svg>
<div class="abs site-name">Melanie Trent, PhD</div>
<ul class="abs nav">
  <li><a class="active" href="#">Home</a></li>
  <li><a href="#">About</a></li>
  <li><a href="#">Store</a></li>
  <li><a href="#">Coming soon</a></li>
  <li><a href="#">Featured in</a></li>
</ul>
<div class="abs header-line"></div>

<div class="abs hero-photo" role="img" aria-label="Photo of a young boy reading the chemistry picture book"></div>
<div class="abs hero-cover" role="img" aria-label="Cover of the children's chemistry book"></div>
<h1 class="abs hero-title"><span class="hl">I had fan</span><br>Learning <span class="hl">About</span><br>ChemistryToday!</h1>
<p class="abs hero-text">Lorem ipsum dolor sit amet, consectet piscing elit. Nam eu ante eget velit eleifend imperdiet et quis urna.</p>
<a class="btn btn-hero" href="#">Buy Book</a>

<!-- About section -->
<h2 class="abs section-title about-title">About Our Book</h2>
<p class="abs body-copy about-copy">Lorem ipsum dolor sit amet, consectetur adipiscing elit. Nam eu ante eget velit eleifend imperdiet et quis urna. Nunc eget metus nec velit luctus sagittis sed quis ex. Aenean quis ultrices ipsum, ut vehicula nunc. Nunc eget nibh ultricies, scelerisque neque eget, blandit dui. Sed vel blandit libero, id eleifend magna. Cras eleifend nulla vel lorem varius,</p>
<a class="btn btn-about" href="#">Read More</a>
<div class="abs about-frame"></div>
<div class="abs about-photo" role="img" aria-label="Photo of a child holding up the chemistry book"></div>
<div class="abs about-badge" role="img" aria-label="Hand-lettered badge: I learned about chemistry today, with cartoon children"></div>

<!-- Book section background -->
<svg class="band" style="top:870px" width="1200" height="520" viewBox="0 0 1200 520" aria-hidden="true">
  <path d="M0 10C120 -5 230 30 380 25C560 18 700 -10 880 5C1000 15 1100 28 1200 22V520H0Z" fill="var(--cream)"/>
</svg>
<div class="abs book-cover" role="img" aria-label="Illustrated cover of the chemistry picture book"></div>
<h2 class="abs section-title book-title">Our Book</h2>
<p class="abs body-copy book-copy">Lorem ipsum dolor sit amet, consectetur adipiscing elit. Nam eu ante eget velit eleifend imperdiet et quis urna. Nunc eget metus nec velit luctus sagittis sed quis ex. Aenean quis ultrices ipsum, ut vehicula nunc. Nunc eget nibh ultricies, scelerisque neque eget, blandit dui. Sed vel blandit libero, id eleifend magna. Cras eleifend nulla vel lorem varius,</p>
<a class="btn btn-book" href="#">Buy Book</a>

<!-- Stats wave -->
<svg class="band" style="top:1325px" width="1200" height="225" viewBox="0 0 1200 225" aria-hidden="true">
  <path d="M0 50C150 10 300 20 450 45C620 75 780 60 950 40C1070 28 1150 40 1200 50V205C1080 225 960 200 820 190C650 178 520 200 360 190C220 182 100 160 0 150Z" fill="var(--sky)"/>
  <path d="M0 150C100 160 220 182 360 190C520 200 650 178 820 190C960 200 1080 225 1200 205V215C1080 232 960 210 820 200C650 190 520 210 360 200C220 192 100 172 0 162Z" fill="var(--sky-deep)"/>
  <path d="M0 50C150 10 300 20 450 45C620 75 780 60 950 40C1070 28 1150 40 1200 50V42C1150 30 1070 20 950 32C780 52 620 66 450 36C300 12 150 2 0 42Z" fill="var(--sky-deep)"/>
</svg>
<div class="abs stats">
  <div class="stat"><div class="stat-num">15</div><div class="stat-label">Total Groups</div></div>
  <div class="stat"><div class="stat-num">32</div><div class="stat-label">Qualified Teachers</div></div>
  <div class="stat"><div class="stat-num">10</div><div class="stat-label">Years of Experience</div></div>
  <div class="stat"><div class="stat-num">255</div><div class="stat-label">Students Enrolled</div></div>
</div>

<!-- Articles -->
<h2 class="abs section-title articles-title">Our&nbsp; Articles</h2>
<p class="abs articles-intro">Lorem ipsum dolor sit amet, consectetur adipiscing elit. Nam eu ante eget velit eleifend imperdiet et quis</p>

<article class="card" style="left:250px">
  <div class="card-img" role="img" aria-label="Photo of a boy reading the book at home" style="background:linear-gradient(135deg,#6d6864,#b5ab9f)"></div>
  <h3>Lorem ipsum dolor amet, sectetur adipiscing elit</h3>
  <p>Lorem ipsum dolor sit consectetur adipiscing elit. Na affente eget velit eleifend imperdiet et quis urna.</p>
  <svg width="36" height="10" viewBox="0 0 36 10" aria-hidden="true"><path d="M1 5H33M28 1L34 5L28 9" stroke="var(--orange)" stroke-width="1.6" fill="none" stroke-linecap="round"/></svg>
</article>
<article class="card" style="left:490px">
  <div class="card-img" role="img" aria-label="Photo of a toddler looking at the book" style="background:linear-gradient(135deg,#3b2b22,#7c5a45)"></div>
  <h3>Lorem ipsum dolor amet, sectetur adipiscing elit</h3>
  <p>Lorem ipsum dolor sit consectetur adipiscing elit. Na affente eget velit eleifend imperdiet et quis urna.</p>
  <svg width="36" height="10" viewBox="0 0 36 10" aria-hidden="true"><path d="M1 5H33M28 1L34 5L28 9" stroke="var(--orange)" stroke-width="1.6" fill="none" stroke-linecap="round"/></svg>
</article>
<article class="card" style="left:730px">
  <div class="card-img" role="img" aria-label="Photo of a child holding the book" style="background:linear-gradient(135deg,#3d4352,#a3a6ad)"></div>
  <h3>Lorem ipsum dolor amet, sectetur adipiscing elit</h3>
  <p>Lorem ipsum dolor sit consectetur adipiscing elit. Na affente eget velit eleifend imperdiet et quis urna.</p>
  <svg width="36" height="10" viewBox="0 0 36 10" aria-hidden="true"><path d="M1 5H33M28 1L34 5L28 9" stroke="var(--orange)" stroke-width="1.6" fill="none" stroke-linecap="round"/></svg>
</article>

<!-- Footer -->
<svg class="band" style="top:1965px" width="1200" height="205" viewBox="0 0 1200 205" aria-hidden="true">
  <path d="M0 40C150 20 300 10 480 30C650 48 800 20 950 10C1060 4 1140 12 1200 18V205H0Z" fill="var(--coral)"/>
</svg>
<div class="abs footer-name">Melanie Trent, PhD</div>
<ul class="abs social" aria-label="Social links">
  <li style="background:#55acee" aria-label="Social profile 1"></li>
  <li style="background:#3b5998" aria-label="Social profile 2"></li>
  <li style="background:#1ab7ea" aria-label="Social profile 3"></li>
  <li style="background:#cb2027" aria-label="Social profile 4"></li>
  <li style="background:#0e76a8" aria-label="Social profile 5"></li>
</ul>
<p class="abs copyright">Melanie Trent, PhD © 2019 All rights reserved. Terms of Use and Privacy Policy</p>

</body>
</html>
```